Thornbury Cleaning – Website Redesign (Clean, Modern, Trust-Focused)

Thornbury Cleaning — Homepage Redesign Brief

Project Goal

We need a complete redesign of the homepage for our cleaning business, Thornbury Cleaning.
The goal is a clean, modern, trust-building homepage that works equally well for:
• Residential clients
• Commercial clients

The page should feel polished, reliable, easy to navigate, and completely free from clutter, gimmicks, or corporate-sounding fluff.

About Us (Context)

Thornbury Cleaning has operated in Sale, Victoria for over 30 years.
Our brand is built on:
• Reliability
• Convenience
• Long-term trust
• Straightforward, no-nonsense communication

We do not want to look like a large franchise, and we do not want to look cute or playful.
The design must feel modern, practical, confident, and professional.

What We Need Designed — Homepage Only

1. Hero Section

A clean, modern hero area with:
• A simple image or clean background (no clutter, no heavy overlays).
Images from our current site may be helpful, or you may source alternatives.
• Headline suggestion (designer may refine):
“30+ Years of Commercial and Residential Cleaning in Sale”
• Sub-headline suggestion:
“Trusted by locals for three decades.”
• Primary CTA button: Get a Quote

2. Trust-Building Logos

Positioned directly beneath the hero:
• Small, neat logos of organisations we work with
(RLK, Bramwell, Eastvale Regional Care, OPM, etc.)
• A clean Reviewly Reviews block (stars + review count)
• Must be compact, tidy, evenly spaced — not loud or oversized

3. Trust Block / Problem–Solution Copy

This section introduces why hiring cleaners can be stressful and why reliability matters.

Headline example:
“Call the cleaners you can count on.”

We have existing copy for this section.
Please present it in a minimal, breathable, modern layout that is easy to scan.

4. Stats / Counters Section

Three sharp, structured stat boxes:
• 92+ Recurring Clients
• 4,150+ Visits Per Year
• 265+ Pre-Sale / Exit Cleans

These should look clean and understated — not oversized or gimmicky.

5. Values Section

A short section featuring our core values:
• Be Real
• Do It Right
• Have Fun
• Make It Easy

Designer has flexibility with layout.
(Sections 5 and 6 may swap depending on what flows better.)

6. Services Preview

A simple grid or row with links to our main services:
• Commercial Cleaning
• Residential Cleaning
• Window Cleaning
• Steam Cleaning

Small icons or photos are fine — but no clip art or cartoon-style graphics.

7. Footer

A very clean, simple footer with contact details.
No clutter, no heavy visual styling.

Style Requirements

Overall Tone
• Clean
• Modern
• Minimal
• Trust-driven
• Easy to read and navigate

Do NOT use
• Clip art
• Cute or playful icons
• Flowers, sparkles, “feminine” cleaning imagery
• Heavy or overly bold corporate fonts
• Busy backgrounds
• Long paragraphs of text

Reference Material

Current Website (for copy + structure only)

https://thornburycleaning-example.com.au

Rough Canva Mock-Up (layout inspiration only)

(We will upload this separately. It’s not a final design — just a loose concept for spacing/flow.)

Logo

Please use the new Thornbury Cleaning logo (uploaded in files) or a placeholder if needed. Attached is a potential for a new logo or site colours not wedded to the idea though.

What the Homepage Should Communicate

Within seconds, a visitor should understand that:
• We are established
• We are local
• We are reliable
• We make cleaning easy
• Getting a quote is quick and simple

The homepage should feel effortless, trustworthy, and modern.

Deliverable

A complete homepage design layout suitable for WordPress.
Figma, Adobe XD, or a similar design tool is fine.

Target Market(s)

Residential and commercial clients in Sale, Victoria and surrounding Gippsland region. Typical clients include busy households, office managers, receptionists, medical centres, community organisations, local businesses, and real estate/property professionals. Clients value reliability, simplicity, and stress-free long-term cleaning support.

Industry/Entity Type

Cleaning services (Residential & Commercial)

Font styles to use
Sans Serif

Requirements
Must have
• • Clean, modern, minimal layout • A trust-driven design that highlights proof (logos, stats, reviews) near the top • Clear hierarchy and no clutter • A strong hero section with simple messaging and a clear CTA • Trust logos + Reviewly Reviews block directly under the hero • Structured stats/counters section • Values section (Be Real, Do It Right, Have Fun, Make It Easy) • Services preview (Commercial, Residential, Window, Steam/Carpet) • Clean footer with contact details • Use our new Thornbury Cleaning logo (or placeholder if needed) • Easy-to-read typography and spacing • Must feel like a local, real cleaning business — not a franchise
Nice to have
• • An option with centred hero text and an option with left-aligned text • Option to preview hero section with or without a quote form • Subtle use of the navy + gold palette (not heavy or corporate) • Soft, minimal background images (not busy city skylines) • Subtle section dividers or whitespace breaks to improve flow • Slightly rounded card corners for a friendly but still modern feel
Should not have
• • No clip-art, cartoon mops, sparkles, bubbles, or generic cleaning icons • No overly bold, blocky, or corporate fonts • No “mega-city” skylines (we are a regional/rural business) • No heavy overlays, dark gradients, or cluttered hero images • No long paragraphs or dense text blocks • No template-style designs that look generic or AI-generated • No overly feminine, overly masculine, or overly playful designs • No neon colors or high-saturation palettes

```html
<!DOCTYPE html>
<html lang="en">
<head>
<meta charset="utf-8">
<title>Thornbury Cleaning — Home</title>
<link href="https://fonts.googleapis.com/css2?family=Poppins:wght@400;500;600;700&display=swap" rel="stylesheet">
<style>
:root{
  --navy:#1e2b47;
  --navy-deep:#17223a;
  --gold:#b9a03f;
  --gold-soft:#cdb75d;
  --ink:#1b1b1b;
  --muted:#555b66;
  --line:#e4e6ea;
  --white:#ffffff;
}
*{box-sizing:border-box;margin:0;padding:0}
html,body{width:1200px;height:4232px;overflow:hidden}
body{font-family:"Poppins",sans-serif;color:var(--ink);background:var(--white);position:relative}
.btn{display:inline-block;background:var(--gold);color:var(--white);font-weight:500;border-radius:20px;text-decoration:none}
.brand{font-weight:700;color:var(--navy);letter-spacing:.5px;line-height:1}

/* Header */
.site-header{height:110px;display:flex;align-items:center;justify-content:space-between;padding:0 84px}
.site-header .brand{font-size:22px}
.site-header .brand small{display:block;font-size:9px;font-weight:700;letter-spacing:2px;margin-top:4px}
.header-right{display:flex;flex-direction:column;align-items:flex-end;gap:10px}
.contact-strip{display:flex;gap:22px;font-size:11px;color:var(--muted)}
.contact-strip span{display:flex;align-items:center;gap:6px}
.nav-row{display:flex;align-items:center;gap:28px}
.main-nav{display:flex;gap:22px;font-size:12px;font-weight:500}
.main-nav a{color:var(--ink);text-decoration:none}
.main-nav a.active{color:var(--gold)}
.nav-row .btn{font-size:12px;padding:9px 22px}

/* Hero */
.hero{position:absolute;left:20px;top:120px;width:1160px;height:528px;border-radius:16px;overflow:hidden;
  background:linear-gradient(120deg,#3d4148 0%,#5b5f66 40%,#2e3138 75%,#4a4d53 100%);
  display:flex;flex-direction:column;align-items:center;justify-content:center;text-align:center}
.hero::after{content:"";position:absolute;inset:0;background:rgba(20,24,32,.35)}
.hero > *{position:relative;z-index:1}
.hero h1{font-size:62px;font-weight:700;line-height:1.08;color:var(--white)}
.hero h1 .accent{color:var(--gold-soft);display:block}
.hero p{font-size:18px;color:var(--white);margin-top:18px}
.hero .btn{margin-top:26px;font-size:15px;padding:13px 30px}

/* Trust logos */
.trust-row{position:absolute;top:690px;left:80px;right:80px;height:120px;display:flex;align-items:center;justify-content:space-between}
.partner{display:flex;align-items:center;gap:10px;font-weight:600;font-size:18px;color:var(--navy)}
.partner .mark{width:34px;height:34px;background:var(--line);border-radius:4px}
.partner .mark.round{border-radius:50%}
.reviews{display:flex;flex-direction:column;gap:4px}
.reviews .name{font-size:22px;font-weight:600;color:var(--navy)}
.reviews .score{display:flex;align-items:center;gap:8px;font-size:20px;font-weight:600}
.reviews .score small{font-size:11px;font-weight:400;color:var(--muted)}
.stars{display:flex;gap:2px}

/* Intro */
.intro{position:absolute;top:840px;left:0;width:1200px;text-align:center}
.intro h2{font-size:40px;font-weight:700;margin-bottom:34px}
.intro p{font-size:15px;line-height:1.65;color:var(--ink);margin-bottom:4px}
.intro .gold{color:var(--gold);font-weight:600}
.intro .gap{margin-top:18px}

/* Stats */
.stats{position:absolute;top:1248px;left:0;width:1200px;height:340px;background:var(--navy);display:flex;justify-content:center;align-items:center;gap:32px}
.stat-card{width:248px;height:228px;background:var(--white);border-radius:10px;text-align:center;padding-top:26px}
.stat-card h3{font-size:15px;font-weight:600;margin-top:12px}
.stat-card .num{font-size:50px;font-weight:600;color:var(--gold);line-height:1.15;margin-top:6px}
.stat-card p{font-size:10px;color:var(--muted);line-height:1.5;padding:6px 40px 0}

/* Services */
.services-title{position:absolute;top:1640px;left:0;width:1200px;text-align:center;font-size:44px;font-weight:700}
.service{position:absolute;left:80px;width:1040px;height:352px;display:flex;align-items:center;gap:60px}
.service .photo{width:520px;height:352px;flex:none}
.service .copy{flex:1}
.service.flip{flex-direction:row-reverse}
.service.flip .copy{text-align:right}
.service h3{font-size:34px;font-weight:600;margin-bottom:14px}
.service p{font-size:11px;line-height:1.6;color:var(--muted);max-width:440px}
.service.flip p{margin-left:auto}
.service .btn{margin-top:18px;font-size:11px;padding:8px 26px}
.s1{top:1772px}.s2{top:2180px}.s3{top:2588px}.s4{top:3000px}
.ph-commercial{background:linear-gradient(135deg,#2b2d30,#8b8d90 55%,#3a3b3d)}
.ph-residential{background:linear-gradient(135deg,#e9e5dd,#cfc5b4 50%,#f2efe9)}
.ph-window{background:linear-gradient(135deg,#25262a,#5d6a78 50%,#1e1f22)}
.ph-steam{background:linear-gradient(135deg,#eef0f2,#c7cbd0 55%,#d8b93a 100%)}

/* Values */
.values{position:absolute;top:3400px;left:0;width:1200px;height:570px;background:var(--navy);padding:50px 80px 0}
.values h2{font-size:40px;font-weight:600;color:var(--white);margin-bottom:34px}
.value-grid{display:grid;grid-template-columns:512px 512px;gap:40px 16px}
.value-card{background:var(--white);border-radius:10px;height:136px;display:flex;gap:22px;padding:26px 30px}
.value-card svg{flex:none}
.value-card h3{font-size:22px;font-weight:600;margin-bottom:6px}
.value-card p{font-size:11px;line-height:1.55;color:var(--muted)}

/* Footer */
.site-footer{position:absolute;top:3970px;left:0;width:1200px;height:222px;padding:48px 84px 0;display:flex;justify-content:space-between}
.site-footer .brand{font-size:22px}
.follow{margin-top:24px;font-size:12px;font-weight:600}
.socials{display:flex;gap:10px;margin-top:10px}
.socials span{width:16px;height:16px;border-radius:50%;background:var(--navy)}
.foot-col h4{font-size:12px;font-weight:600;color:var(--gold);margin-bottom:12px}
.foot-col li{list-style:none;font-size:11px;color:var(--muted);line-height:1.9}
.foot-col li b{color:var(--ink);font-weight:600}
.copyright{position:absolute;top:4192px;left:0;width:1200px;height:40px;background:var(--navy);color:#cfd3da;font-size:11px;display:flex;align-items:center;justify-content:center}
</style>
</head>
<body>

<header class="site-header">
  <div class="brand">THORNBURY CLEANING<small>EST. 1993</small></div>
  <div class="header-right">
    <div class="contact-strip">
      <span><svg width="12" height="12" viewBox="0 0 24 24" fill="none" stroke="#b9a03f" stroke-width="2"><path d="M5 3h4l2 5-3 2a12 12 0 0 0 6 6l2-3 5 2v4a2 2 0 0 1-2 2A18 18 0 0 1 3 5a2 2 0 0 1 2-2z"/></svg>Call us: 0400 123 456</span>
      <span><svg width="12" height="12" viewBox="0 0 24 24" fill="none" stroke="#b9a03f" stroke-width="2"><rect x="3" y="5" width="18" height="14" rx="2"/><path d="M3 7l9 6 9-6"/></svg>Email us</span>
    </div>
    <div class="nav-row">
      <nav class="main-nav"><a class="active" href="#">HOME</a><a href="#">ABOUT</a><a href="#">SERVICES</a><a href="#">CONTACT</a></nav>
      <a class="btn" href="#">Get a Quote</a>
    </div>
  </div>
</header>

<section class="hero" role="img" aria-label="Cleaner wiping down a bright modern office">
  <h1>30+ Years of<span class="accent">Commercial and Residential<br>Cleaning in Sale</span></h1>
  <p>Trusted by locals for three decades.</p>
  <a class="btn" href="#">Get a Quote</a>
</section>

<section class="trust-row">
  <div class="partner"><span class="mark"></span>RLK</div>
  <div class="partner">Bramwell</div>
  <div class="partner"><span class="mark round"></span>Eastvale Regional Care</div>
  <div class="partner"><span class="mark"></span>OPM</div>
  <div class="reviews">
    <div class="name">Reviewly</div>
    <div class="score">
      <div class="stars">
        <svg width="20" height="20" viewBox="0 0 24 24"><path fill="#f3b400" d="M12 2l3 7 7 .6-5.3 4.6 1.6 7.3L12 17.8 5.7 21.5l1.6-7.3L2 9.6 9 9z"/></svg>
        <svg width="20" height="20" viewBox="0 0 24 24"><path fill="#f3b400" d="M12 2l3 7 7 .6-5.3 4.6 1.6 7.3L12 17.8 5.7 21.5l1.6-7.3L2 9.6 9 9z"/></svg>
        <svg width="20" height="20" viewBox="0 0 24 24"><path fill="#f3b400" d="M12 2l3 7 7 .6-5.3 4.6 1.6 7.3L12 17.8 5.7 21.5l1.6-7.3L2 9.6 9 9z"/></svg>
        <svg width="20" height="20" viewBox="0 0 24 24"><path fill="#f3b400" d="M12 2l3 7 7 .6-5.3 4.6 1.6 7.3L12 17.8 5.7 21.5l1.6-7.3L2 9.6 9 9z"/></svg>
        <svg width="20" height="20" viewBox="0 0 24 24"><path fill="#f3b400" d="M12 2l3 7 7 .6-5.3 4.6 1.6 7.3L12 17.8 5.7 21.5l1.6-7.3L2 9.6 9 9z"/></svg>
      </div>
      4.7 <small>(26 Reviews)</small>
    </div>
  </div>
</section>

<section class="intro">
  <h2>Call the cleaners you can count on</h2>
  <p>When you need help cleaning, the last thing you want is more stress.</p>
  <p class="gold">Too often, that’s exactly what happens –</p>
  <p>Cleaners don’t show up. Jobs get rushed or half done. And you’re left <span class="gold">wondering why you didn’t just do it yourself.</span></p>
  <p class="gap">You shouldn’t have to second-guess whether the job will be done right.</p>
  <p>You should be able to <span class="gold">book it, forget it, and trust it’s sorted — properly.</span></p>
  <p class="gap"><span class="gold">Trusted by locals for 30+ years</span> to deliver reliable, long-term cleaning — the kind you never have to second-guess.</p>
</section>

<section class="stats">
  <div class="stat-card">
    <svg width="44" height="44" viewBox="0 0 24 24" fill="none" stroke="#b9a03f" stroke-width="1.5"><path d="M3 11l9-7 9 7"/><path d="M5 10v10h14V10"/><path d="M10 20v-5h4v5"/></svg>
    <h3>Recurring Clients</h3>
    <div class="num">92+</div>
    <p>Everyday support safety and companionship at home</p>
  </div>
  <div class="stat-card">
    <svg width="44" height="44" viewBox="0 0 24 24" fill="none" stroke="#b9a03f" stroke-width="1.5"><rect x="3" y="5" width="18" height="16" rx="2"/><path d="M3 10h18M8 3v4M16 3v4"/></svg>
    <h3>Visits Per Year</h3>
    <div class="num">4,150+</div>
    <p>Everyday support safety and companionship at home</p>
  </div>
  <div class="stat-card">
    <svg width="44" height="44" viewBox="0 0 24 24" fill="none" stroke="#b9a03f" stroke-width="1.5"><path d="M3 7l9-4 9 4v10l-9 4-9-4z"/><path d="M3 7l9 4 9-4M12 11v10"/></svg>
    <h3>Pre-Sale / Exit Cleans</h3>
    <div class="num">265+</div>
    <p>Everyday support safety and companionship at home</p>
  </div>
</section>

<h2 class="services-title">What We Clean</h2>

<article class="service s1">
  <div class="photo ph-commercial" role="img" aria-label="Empty modern office corridor with glass walls"></div>
  <div class="copy">
    <h3>Commercial Cleaning</h3>
    <p>Keep your offices, clinics and shared spaces spotless with reliable after-hours cleaning that suits your roster, your budget and your standards, week after week without fuss.</p>
    <a class="btn" href="#">Start Here</a>
  </div>
</article>

<article class="service s2 flip">
  <div class="photo ph-residential" role="img" aria-label="Bright tidy living room with cream sofa"></div>
  <div class="copy">
    <h3>Residential Cleaning</h3>
    <p>Come home to a fresh, tidy house without lifting a finger. Our friendly local team handles the weekly clean so you can focus on what matters.</p>
    <a class="btn" href="#">Start Here</a>
  </div>
</article>

<article class="service s3">
  <div class="photo ph-window" role="img" aria-label="Clean window glass with trees behind"></div>
  <div class="copy">
    <h3>Window Cleaning</h3>
    <p>Keep streaky windows out of sight. We clean glass inside and out, frames and tracks included, so your home or shopfront lets in every bit of light.</p>
    <a class="btn" href="#">Start Here</a>
  </div>
</article>

<article class="service s4 flip">
  <div class="photo ph-steam" role="img" aria-label="Gloved hand using a steam cleaner"></div>
  <div class="copy">
    <h3>Steam Cleaning</h3>
    <p>Lift deep stains and lingering odours from carpets and upholstery. Our steam cleaning restores fibres, dries quickly and leaves rooms fresh for move-in or sale.</p>
    <a class="btn" href="#">Start Here</a>
  </div>
</article>

<section class="values">
  <h2>Our core values</h2>
  <div class="value-grid">
    <div class="value-card">
      <svg width="56" height="56" viewBox="0 0 24 24" fill="#b9a03f"><path d="M3 8l4 4 5-7 5 7 4-4-2 11H5z"/></svg>
      <div><h3>Be Real</h3><p>Lorem Ipsum is simply dummy text of the printing and typesetting industry. Lorem Ipsum has been the industry's standard dummy text ever since the 1500s.</p></div>
    </div>
    <div class="value-card">
      <svg width="56" height="56" viewBox="0 0 24 24" fill="none" stroke="#b9a03f" stroke-width="1.5"><circle cx="12" cy="8" r="4"/><path d="M4 21a8 8 0 0 1 16 0"/></svg>
      <div><h3>Do It Right</h3><p>Lorem Ipsum is simply dummy text of the printing and typesetting industry. Lorem Ipsum has been the industry's standard dummy text ever since the 1500s.</p></div>
    </div>
    <div class="value-card">
      <svg width="56" height="56" viewBox="0 0 24 24" fill="none" stroke="#b9a03f" stroke-width="1.5"><circle cx="12" cy="12" r="9"/><path d="M8 14a5 5 0 0 0 8 0"/><circle cx="9" cy="10" r=".8" fill="#b9a03f"/><circle cx="15" cy="10" r=".8" fill="#b9a03f"/></svg>
      <div><h3>Have Fun</h3><p>Lorem Ipsum is simply dummy text of the printing and typesetting industry. Lorem Ipsum has been the industry's standard dummy text ever since the 1500s.</p></div>
    </div>
    <div class="value-card">
      <svg width="56" height="56" viewBox="0 0 24 24" fill="none" stroke="#b9a03f" stroke-width="1.5"><circle cx="12" cy="12" r="9"/><path d="M8 12l3 3 5-6"/></svg>
      <div><h3>Make It Easy</h3><p>Lorem Ipsum is simply dummy text of the printing and typesetting industry. Lorem Ipsum has been the industry's standard dummy text ever since the 1500s.</p></div>
    </div>
  </div>
</section>

<footer class="site-footer">
  <div>
    <div class="brand">THORNBURY CLEANING</div>
    <div class="follow">FOLLOW US</div>
    <div class="socials"><span></span><span></span><span></span><span></span><span></span></div>
  </div>
  <div class="foot-col"><h4>QUICK LINKS</h4><ul><li>Home</li><li>About Us</li><li>Blog</li><li>FAQs</li></ul></div>
  <div class="foot-col"><h4>SERVICES</h4><ul><li>Commercial Cleaning</li><li>Residential Cleaning</li><li>Window Cleaning</li><li>Steam Cleaning</li></ul></div>
  <div class="foot-col"><h4>CONTACT US</h4><ul>
    <li><b>Phone:</b> 0400 123 456</li>
    <li><b>Email:</b> info@thornburycleaning-example.com.au</li>
    <li><b>ABN:</b> 00 000 000 000</li>
    <li><b>Address:</b> 12 Sample Street, Sale Victoria 3850</li>
  </ul></div>
</footer>
<div class="copyright">© 2024–2025 Thornbury Cleaning</div>

</body>
</html>
```